Window Treatment business needs website redesigned.

We need a revamp and refresh of our current site www.velmorin.ca
Looking to attract very high end customer. It should be a very simple design with very little text. This site will be visited by prospective homeowners, designers, builders and architects. They should feel that they are dealing with a high-end product selection, where experience, customer service and unique product offering is the focus. The content will be to highlight our services and highlight the manufacturers we sell, using a few rich photos to highlight the products. We should NOT look like we are a very large company. It should NOT have discounts/savings buttons and many menus to choose from. We offer over 15 years experience to narrow the many market options, to provide the right technical solution.
We specialize in products that are not readily available on the market and specifically motorized systems for indoors and outdoors.
Our main suppliers are Quarnel.com, Dexavo.com
We carry our own locally manufactured product line of roller shades.
Main product pictures should be of roller shades, outdoor bug screens, awnings and outdoor pergolas.

Reason: I understand that Christmas is coming up real short and many people are extremely busy. If you have a CREATIVE gifting you still want to submit, I look forward to your idea!

Reason: Due to holiday season, we have not had sufficient time to review to make a final decision. Thank you for your patience!

Target Market(s)

High end home owners, designers, builders, architects

Industry/Entity Type

Contractor

Coding

Coded - Design and coding required

Number of Pages Required

3 page

Font styles to use
Sans Serif

Requirements
Must have
• Landing page with full size image like homepage of borvela.it
• Products page that highlights products with simple product shot image, description and link to manufacturer.
• On main page a scrolling of customer reviews.
• I want a very simple, eye-catching, emotional image for homepage. It does not need to include any product image.
• An image that shows technology combining/meshing with hand craftsmanship.
• Focus is on design.
• http://www.borvela.it/en/gallery is a great layout and design.
Nice to have
• Logo shape for icons and watermark should be used.
• Look like and have simple motion effects like tirquel.com or manvexo.com
Should not have
• Generic/standard looking feel like gostrel.com or plinkwardcove.ca
• No use of green as background only subtle text.
• Lots of text and pages.

```html
<!DOCTYPE html>
<html lang="en">
<head>
<meta charset="utf-8">
<title>Velmorin — Window Treatment Solutions</title>
<link href="https://fonts.googleapis.com/css2?family=Raleway:wght@400;500;600;700&display=swap" rel="stylesheet">
<style>
  :root {
    --white: #ffffff;
    --soft-white: rgba(255,255,255,0.82);
    --muted: rgba(255,255,255,0.6);
    --line: rgba(255,255,255,0.22);
    --band: rgba(20,20,20,0.55);
    --tile: rgba(18,22,18,0.62);
    --green-text: #8dc63f;
    --star: #f58220;
    --photo-top: #4a3f33;
    --photo-mid: #5d6a5c;
    --photo-low: #3a4034;
    --photo-base: #1f211c;
  }
  * { margin: 0; padding: 0; box-sizing: border-box; }
  html, body { width: 1200px; height: 600px; overflow: hidden; background: #111; }
  body { font-family: "Raleway", sans-serif; color: var(--white); }

  .hero { position: relative; width: 1200px; height: 600px; overflow: hidden; }
  .hero-photo {
    position: absolute; inset: 0;
    background:
      linear-gradient(180deg, rgba(0,0,0,0.35) 0%, rgba(0,0,0,0.2) 45%, rgba(0,0,0,0.55) 100%),
      linear-gradient(170deg, var(--photo-top) 0%, #5a4c3d 28%, var(--photo-mid) 48%, var(--photo-low) 72%, var(--photo-base) 100%);
  }

  .site-header {
    position: absolute; left: 0; top: 0; width: 1200px; height: 79px;
    border-bottom: 1px solid var(--line);
  }
  .brand { position: absolute; left: 99px; top: 12px; display: flex; align-items: center; gap: 8px; }
  .brand-mark { width: 54px; height: 54px; border: 3px solid var(--white); border-radius: 50%; }
  .brand-text { display: flex; flex-direction: column; }
  .brand-name { font-size: 29px; font-weight: 500; line-height: 1; letter-spacing: 0.5px; }
  .brand-tagline { font-size: 11px; font-weight: 500; margin-top: 3px; }

  .main-nav { position: absolute; right: 99px; top: 32px; display: flex; gap: 51px; }
  .main-nav a { color: var(--white); text-decoration: none; font-size: 14px; font-weight: 500; }

  .headline {
    position: absolute; left: 99px; top: 204px;
    font-size: 43px; font-weight: 700; letter-spacing: 0.3px;
  }
  .subline { position: absolute; left: 99px; top: 266px; font-size: 17px; font-weight: 500; }

  .intro-band { position: absolute; left: 0; top: 343px; width: 566px; height: 147px; background: var(--band); }
  .intro-text {
    position: absolute; left: 99px; top: 24px; width: 460px;
    font-size: 12px; line-height: 21px; color: var(--soft-white);
  }
  .rating { position: absolute; left: 99px; top: 104px; display: flex; align-items: center; }
  .stars { display: flex; gap: 2px; }
  .stars svg { width: 15px; height: 15px; fill: var(--star); }
  .review-count { margin-left: 27px; font-size: 12px; color: var(--green-text); }
  .slide-dots { position: absolute; left: 462px; top: 108px; display: flex; gap: 7px; }
  .slide-dots span { width: 10px; height: 10px; border: 1px solid var(--white); border-radius: 50%; }

  .slide-arrow { position: absolute; top: 286px; width: 20px; height: 30px; }
  .slide-arrow.prev { left: 16px; }
  .slide-arrow.next { right: 16px; }

  .treatment-diagram { position: absolute; left: 660px; top: 90px; width: 460px; height: 430px; }
  .tile-icon { fill: none; stroke: var(--green-text); stroke-width: 2; }
  .tile-label { fill: var(--white); font-size: 12px; font-weight: 500; }

  .site-footer {
    position: absolute; left: 0; top: 540px; width: 1200px; height: 60px;
    border-top: 1px solid var(--line);
  }
  .copyright { position: absolute; left: 98px; top: 24px; font-size: 12px; color: var(--muted); }
  .social-links { position: absolute; left: 908px; top: 17px; display: flex; gap: 7px; }
  .social-links span { width: 26px; height: 26px; border: 1px solid var(--muted); border-radius: 50%; }
</style>
</head>
<body>
<div class="hero">
  <div class="hero-photo" role="img" aria-label="Photo of a terrace under a motorized awning overlooking a lake and green hills"></div>

  <header class="site-header">
    <div class="brand">
      <span class="brand-mark"></span>
      <div class="brand-text">
        <span class="brand-name">Velmorin</span>
        <span class="brand-tagline">Window Treatment Solutions</span>
      </div>
    </div>
    <nav class="main-nav">
      <a href="#">HOME</a>
      <a href="#">GALLERY</a>
      <a href="#">CONTACT</a>
    </nav>
  </header>

  <h1 class="headline">We Do Window Treatment</h1>
  <p class="subline">15 Years Experience Serving The Design/Build Industry</p>

  <section class="intro-band">
    <p class="intro-text">we specialize in custom high quality window treatments. Whether it is for a condo, home or entire building, we provide free sampling, free on site consultation and turn-key installation services to Toronto</p>
    <div class="rating">
      <div class="stars">
        <svg viewBox="0 0 20 20"><polygon points="10,1 12.6,7 19,7.4 14,11.6 15.6,18 10,14.5 4.4,18 6,11.6 1,7.4 7.4,7"/></svg>
        <svg viewBox="0 0 20 20"><polygon points="10,1 12.6,7 19,7.4 14,11.6 15.6,18 10,14.5 4.4,18 6,11.6 1,7.4 7.4,7"/></svg>
        <svg viewBox="0 0 20 20"><polygon points="10,1 12.6,7 19,7.4 14,11.6 15.6,18 10,14.5 4.4,18 6,11.6 1,7.4 7.4,7"/></svg>
        <svg viewBox="0 0 20 20"><polygon points="10,1 12.6,7 19,7.4 14,11.6 15.6,18 10,14.5 4.4,18 6,11.6 1,7.4 7.4,7"/></svg>
        <svg viewBox="0 0 20 20"><polygon points="10,1 12.6,7 19,7.4 14,11.6 15.6,18 10,14.5 4.4,18 6,11.6 1,7.4 7.4,7"/></svg>
      </div>
      <span class="review-count">365 Commends</span>
    </div>
    <div class="slide-dots"><span></span><span></span><span></span><span></span><span></span></div>
  </section>

  <svg class="slide-arrow prev" viewBox="0 0 20 30"><polyline points="16,1 3,15 16,29" fill="none" stroke="#fff" stroke-width="1.2"/></svg>
  <svg class="slide-arrow next" viewBox="0 0 20 30"><polyline points="4,1 17,15 4,29" fill="none" stroke="#fff" stroke-width="1.2"/></svg>

  <svg class="treatment-diagram" viewBox="660 90 460 430" font-family="Raleway, sans-serif">
    <defs>
      <polygon id="oct-fill" points="46,19 19,46 -19,46 -46,19 -46,-19 -19,-46 19,-46 46,-19"/>
      <polygon id="oct-frame" points="54,22 22,54 -22,54 -54,22 -54,-22 -22,-54 22,-54 54,-22"/>
      <marker id="arrow-head" viewBox="0 0 6 6" refX="5" refY="3" markerWidth="5" markerHeight="5" orient="auto">
        <path d="M0,0 L6,3 L0,6 Z" fill="#fff"/>
      </marker>
    </defs>

    <g class="flow-arrows" fill="none" stroke="#fff" stroke-width="1.2" marker-end="url(#arrow-head)">
      <path d="M866,118 L880,128"/>
      <path d="M1007,154 L1007,170"/>
      <path d="M1096,276 L1076,290"/>
      <path d="M1097,413 L1036,413"/>
      <path d="M941,503 L917,485"/>
      <path d="M787,472 L787,436"/>
      <path d="M690,396 L690,355"/>
      <path d="M684,215 L702,196"/>
    </g>

    <g class="treatment-tile" transform="translate(828,156)">
      <use href="#oct-frame" fill="none" stroke="#fff" stroke-width="1.3"/>
      <use href="#oct-fill" fill="var(--tile)"/>
      <g class="tile-icon"><rect x="-7" y="-28" width="14" height="16" rx="2"/><line x1="0" y1="-33" x2="0" y2="-28"/><line x1="-3" y1="-8" x2="3" y2="-8"/></g>
      <text class="tile-label" x="0" y="12" text-anchor="middle">Motorized</text>
      <text class="tile-label" x="0" y="29" text-anchor="middle">systems</text>
    </g>

    <g class="treatment-tile" transform="translate(950,154)">
      <use href="#oct-frame" fill="none" stroke="#fff" stroke-width="1.3"/>
      <use href="#oct-fill" fill="var(--tile)"/>
      <g class="tile-icon"><polyline points="-16,-20 0,-28 16,-20"/><line x1="0" y1="-24" x2="0" y2="-10"/><line x1="-8" y1="-10" x2="8" y2="-10"/></g>
      <text class="tile-label" x="0" y="12" text-anchor="middle">Indoors</text>
      <text class="tile-label" x="0" y="29" text-anchor="middle">Treatment</text>
    </g>

    <g class="treatment-tile" transform="translate(1040,247)">
      <use href="#oct-frame" fill="none" stroke="#fff" stroke-width="1.3"/>
      <use href="#oct-fill" fill="var(--tile)"/>
      <g class="tile-icon"><rect x="-16" y="-31" width="32" height="23"/><line x1="-6" y1="-31" x2="-6" y2="-8"/><line x1="6" y1="-31" x2="6" y2="-8"/></g>
      <text class="tile-label" x="0" y="12" text-anchor="middle">Outdoors</text>
      <text class="tile-label" x="0" y="29" text-anchor="middle">Treatment</text>
    </g>

    <g class="treatment-tile" transform="translate(1043,360)">
      <use href="#oct-frame" fill="none" stroke="#fff" stroke-width="1.3"/>
      <use href="#oct-fill" fill="var(--tile)"/>
      <g class="tile-icon"><rect x="-5" y="-33" width="8" height="11" rx="1"/><rect x="-11" y="-21" width="20" height="8" rx="2"/><line x1="0" y1="-13" x2="0" y2="-6"/></g>
      <text class="tile-label" x="0" y="12" text-anchor="middle">Roller Shades</text>
      <text class="tile-label" x="0" y="29" text-anchor="middle">Treatment</text>
    </g>

    <g class="treatment-tile" transform="translate(964,452)">
      <use href="#oct-frame" fill="none" stroke="#fff" stroke-width="1.3"/>
      <use href="#oct-fill" fill="var(--tile)"/>
      <g class="tile-icon"><circle cx="0" cy="-19" r="11"/><line x1="0" y1="-30" x2="0" y2="-8"/></g>
      <text class="tile-label" x="0" y="12" text-anchor="middle">Outdoor Bug</text>
      <text class="tile-label" x="0" y="29" text-anchor="middle">Screens</text>
    </g>

    <g class="treatment-tile" transform="translate(843,449)">
      <use href="#oct-frame" fill="none" stroke="#fff" stroke-width="1.3"/>
      <use href="#oct-fill" fill="var(--tile)"/>
      <g class="tile-icon"><rect x="-7" y="-28" width="14" height="16" rx="2"/><line x1="0" y1="-33" x2="0" y2="-28"/><line x1="-3" y1="-8" x2="3" y2="-8"/></g>
      <text class="tile-label" x="0" y="12" text-anchor="middle">Awnings</text>
      <text class="tile-label" x="0" y="29" text-anchor="middle">Treatment</text>
    </g>

    <g class="treatment-tile" transform="translate(747,370)">
      <use href="#oct-frame" fill="none" stroke="#fff" stroke-width="1.3"/>
      <use href="#oct-fill" fill="var(--tile)"/>
      <g class="tile-icon"><rect x="-14" y="-32" width="28" height="8"/><rect x="-12" y="-24" width="24" height="17"/><rect x="-5" y="-17" width="10" height="10"/></g>
      <text class="tile-label" x="0" y="12" text-anchor="middle">Outdoor</text>
      <text class="tile-label" x="0" y="29" text-anchor="middle">Pergolas.</text>
    </g>

    <g class="treatment-tile" transform="translate(734,245)">
      <use href="#oct-frame" fill="none" stroke="#fff" stroke-width="1.3"/>
      <use href="#oct-fill" fill="var(--tile)"/>
      <circle class="tile-icon" cx="0" cy="-20" r="13"/>
      <text class="tile-label" x="0" y="12" text-anchor="middle">Manufactured</text>
      <text class="tile-label" x="0" y="29" text-anchor="middle">Products</text>
    </g>

    <text x="891" y="300" text-anchor="middle" font-size="26" font-weight="700" fill="#fff">OUR WINDOW</text>
    <text x="891" y="335" text-anchor="middle" font-size="26" font-weight="700" fill="#fff">TREATMENT</text>
  </svg>

  <footer class="site-footer">
    <p class="copyright">Copyrights@2016Company Name , all rights reserved</p>
    <div class="social-links"><span></span><span></span><span></span><span></span><span></span><span></span></div>
  </footer>
</div>
</body>
</html>
```